Loyalty Harbor Social Media offering

Immediately need (within 18 hrs) a 5.5" x 4" size ad for a magazine. Overall, we want the design to be simple for branding and to highlight our new offering of proactive social media review management to drive 5* review management over the major consumer platforms, SEEKORA - FRIENDLOOP _ PX - etc. We provide a robust open platform for owners, site managers and the support team to be able to not only respond to all reviews from 1* to 5* but also solicit 5* reviews through our day to day interaction with their customer base.

The primary reviews that our customers get are from Seekora, Friendloop and Pixagram that the public may respond back. The goal is to of course drive 5 star reviews!! Visit our website www.loyaltyharbor-demo.com to see the use of our gradient colors.

Target Market(s)

Owner and operators along with marketing team that manages social media for car wash operators that we also support membership management of the subscriptions through cancelations. We leverage a dedicated support team of live agents along with heavy use of AI to support our brands. The goal is to create a high touch point, customer support while driving retention efforts and 5 Star reviews.

Industry/Entity Type

BPO, call center service, white label service, Express Car Wash

Font styles to use
Other font styles liked:
• poppins

Colors
0054AA
0677BA
7BADD7
CADEEF
E8F1F8
FFC000
F8CF3A
FAE287
FDF2CF
FEFAEE
F0912C
F2A743
F7CA91
FBE8D2
FDF5EE

Requirements
Must have
• 300 DPI, Adobe PDF file. 5.5" W x 4"H with .125" bleed. My logo, express car wash image in the back ground, use of navy blue and gradient colors in brand. You can reference the platform we use https://quillnest-demo.com/ to pick up selling points around the offering. Do not mention Quillnest though as our product is white labeled to our customer
Nice to have
• 2nd version in a 72"w x 24" graphic, 300 dpi, adobe file. Appropriate images related to social media that sell the review management process and proactive nature to solicit 5* reviews to the strategic customer base. I included the last direct mail size piece we created for art that we liked. This piece is a little more specific so needs to have some look and feel of different
Should not have
• yellow color, green, etc

```html
<!DOCTYPE html>
<html lang="en">
<head>
<meta charset="UTF-8">
<title>Loyalty Harbor – Review Management Ad</title>
<link href="https://fonts.googleapis.com/css2?family=Poppins:wght@300;400;500;600;700;800&display=swap" rel="stylesheet">
<style>
  :root{
    --navy:#0b1f4f;
    --navy-deep:#04153a;
    --brand-blue:#0677ba;
    --bright-blue:#0a6fc4;
    --sky:#3a9ae0;
    --orange:#f26c22;
    --amber:#fbb21a;
    --ink:#1b1b1b;
    --white:#ffffff;
    --backdrop:#e9e9e9;
  }
  *{box-sizing:border-box;margin:0;padding:0}
  html,body{width:1200px;height:1200px;overflow:hidden}
  body{background:var(--backdrop);font-family:'Poppins',sans-serif;position:relative}
  .ad{position:absolute;left:0;top:164px;width:1200px;height:872px;background:var(--white);overflow:hidden}

  .brand{position:absolute;left:68px;top:54px;display:flex;align-items:center;gap:16px}
  .brand-dot{width:58px;height:58px;border-radius:50%;background:linear-gradient(135deg,var(--orange),var(--amber))}
  .brand-name{font-weight:700;font-size:38px;color:var(--navy);letter-spacing:1px;text-transform:uppercase}

  .hero{position:absolute;left:0;top:154px;width:1200px;height:477px;
    background:linear-gradient(90deg,var(--navy-deep) 0%,#0b3a86 45%,var(--bright-blue) 100%)}
  .hero-photo{position:absolute;left:710px;top:36px;width:415px;height:595px;
    background:linear-gradient(180deg,#d9b8a4 0%,#3a3a55 40%,#1a1a22 100%)}

  .headline{position:absolute;left:62px;top:188px;color:var(--white);line-height:1.08}
  .headline .lead{font-weight:400;font-size:44px;letter-spacing:3px;display:block}
  .headline .accent{font-weight:800;font-size:57px;display:block;
    background:linear-gradient(90deg,var(--orange),var(--amber));-webkit-background-clip:text;background-clip:text;color:transparent}
  .headline .close{font-weight:800;font-size:46px;display:block}

  .dots{position:absolute;display:flex;gap:5px}
  .dots span{width:10px;height:10px;border-radius:50%;background:var(--sky)}
  .dots.row-left{left:67px;top:370px}
  .dots.row-right{left:542px;top:377px}
  .dots.row-right span{width:12px;height:12px;background:#5bb6f0}

  .offer-tag{position:absolute;left:67px;top:402px;width:330px;height:37px;border-radius:0 20px 20px 0;
    background:linear-gradient(90deg,var(--orange),var(--amber));color:var(--ink);
    font-weight:700;font-size:25px;line-height:37px;padding-left:21px}
  .offer-frame{position:absolute;left:405px;top:419px}

  .offer-copy{position:absolute;left:67px;top:459px;color:var(--white);font-size:21px;line-height:28px;font-weight:400}
  .offer-divider{position:absolute;left:383px;top:463px;width:1.5px;height:76px;background:var(--white)}
  .offer-badge{position:absolute;left:415px;top:460px;color:var(--white);font-weight:700;font-size:20px;line-height:26px}
  .stars{display:flex;gap:3px;margin-bottom:8px}

  .platforms{position:absolute;left:68px;top:556px;color:var(--white);font-size:17px;font-weight:500;display:flex;gap:14px;align-items:center}
  .platforms .names{font-weight:600;font-size:15px;color:#bfe0fa}

  .tagline{position:absolute;left:69px;top:651px;font-weight:700;font-size:24px;line-height:30px;text-transform:uppercase}
  .tagline .dark{color:var(--ink);display:block}
  .tagline .blue{color:var(--brand-blue);display:block}
  .foot-divider{position:absolute;left:331px;top:654px;width:1.5px;height:92px;background:var(--ink)}
  .stat{position:absolute;left:369px;top:655px;width:770px;font-size:20px;line-height:26px;color:var(--ink);font-weight:400}

  .contact{position:absolute;left:70px;top:758px;display:flex;align-items:center}
  .icon-circle{width:40px;height:40px;border-radius:50%;background:var(--orange);display:flex;align-items:center;justify-content:center}
  .phone{font-weight:700;font-size:43px;color:var(--ink);margin:0 18px 0 20px}
  .web{font-weight:700;font-size:37px;color:var(--ink);margin-left:14px}
  .web .domain{color:var(--brand-blue)}
</style>
</head>
<body>
<main class="ad">
  <div class="brand">
    <span class="brand-dot"></span>
    <span class="brand-name">Loyalty Harbor</span>
  </div>

  <section class="hero">
    <h1 class="headline" style="top:34px">
      <span class="lead">HOW YOUR</span>
      <span class="accent">CUSTOMER EXITS</span>
      <span class="close">REALLY DOES MATTER!</span>
    </h1>

    <div class="dots row-left" style="top:216px"><span></span><span></span><span></span><span></span><span></span><span></span></div>
    <div class="dots row-right" style="top:223px"><span></span><span></span><span></span></div>

    <div class="offer-tag" style="top:248px">OUR NEW OFFERING</div>
    <svg class="offer-frame" style="top:263px" width="340" height="150" viewBox="0 0 340 150">
      <path d="M0 2 H225 Q255 2 255 32 V140 H240" fill="none" stroke="#fff" stroke-width="1.5"/>
    </svg>

    <p class="offer-copy" style="top:305px">Generate more 5 Star<br>Reviews through a<br>dedicated support team</p>
    <div class="offer-divider" style="top:309px"></div>
    <div class="offer-badge" style="top:306px">
      <div class="stars">
        <svg width="128" height="22" viewBox="0 0 128 22">
          <defs><linearGradient id="starFill" x1="0" y1="0" x2="0" y2="1"><stop offset="0" stop-color="#ffd23f"/><stop offset="1" stop-color="#f5a300"/></linearGradient></defs>
          <g fill="url(#starFill)">
            <polygon points="11,1 13.6,8 21,8 15,12.5 17.3,20 11,15.5 4.7,20 7,12.5 1,8 8.4,8"/>
            <polygon transform="translate(26 0)" points="11,1 13.6,8 21,8 15,12.5 17.3,20 11,15.5 4.7,20 7,12.5 1,8 8.4,8"/>
            <polygon transform="translate(52 0)" points="11,1 13.6,8 21,8 15,12.5 17.3,20 11,15.5 4.7,20 7,12.5 1,8 8.4,8"/>
            <polygon transform="translate(78 0)" points="11,1 13.6,8 21,8 15,12.5 17.3,20 11,15.5 4.7,20 7,12.5 1,8 8.4,8"/>
            <polygon transform="translate(104 0)" points="11,1 13.6,8 21,8 15,12.5 17.3,20 11,15.5 4.7,20 7,12.5 1,8 8.4,8"/>
          </g>
        </svg>
      </div>
      5 STAR REVIEW<br>MANAGEMENT
    </div>

    <div class="platforms" style="top:402px">
      <span>OVER THE MAJOR CONSUMER PLATFORMS</span>
      <span class="names">Seekora · Friendloop · Pixagram</span>
    </div>

    <div class="hero-photo" role="img" aria-label="Smiling customer support agent wearing a headset, arms crossed, in a dark blazer and blue blouse" style="top:-118px"></div>
  </section>

  <div class="tagline">
    <span class="dark">THE BEST OF THE</span>
    <span class="blue">HUMAN TOUCH</span>
    <span class="blue">AND AI</span>
  </div>
  <div class="foot-divider"></div>
  <p class="stat">Somewhere this data point a significant majority of consumers, around 70-80%, still prefer speaking to a human representative rather than interacting with an automated system.</p>

  <div class="contact">
    <span class="icon-circle">
      <svg width="22" height="22" viewBox="0 0 24 24"><path fill="#fff" d="M6.6 10.8a15.1 15.1 0 0 0 6.6 6.6l2.2-2.2c.3-.3.7-.4 1-.2 1.1.4 2.3.6 3.6.6.6 0 1 .4 1 1V20c0 .6-.4 1-1 1A17 17 0 0 1 3 4c0-.6.4-1 1-1h3.5c.6 0 1 .4 1 1 0 1.3.2 2.5.6 3.6.1.3 0 .7-.2 1z"/></svg>
    </span>
    <span class="phone">555.014.0199</span>
    <span class="icon-circle">
      <svg width="24" height="24" viewBox="0 0 24 24" fill="none" stroke="#fff" stroke-width="1.6"><circle cx="12" cy="12" r="9"/><ellipse cx="12" cy="12" rx="4" ry="9"/><path d="M3 12h18M4.5 7.5h15M4.5 16.5h15"/></svg>
    </span>
    <span class="web">www.<span class="domain">loyaltyharbor-demo</span>.com</span>
  </div>
</main>
</body>
</html>
```